Letterhead for 3 attorney Workers' Comp law firm

We are a 3 attorney law office. We specialize in Workers' Compensation. Our office represents workers who are injured on the job, and the estates of workers who are killed one the job.
When we started our office, we created our own letterhead & have been using it for years. We've just recently hired the 3rd attorney, and were going to just add his name to the letterhead, but have decided we wanted to get a professionally designed letterhead and business cards at this point.
We want something that looks clean and professional. It must look good in black and white because we often make multiple copies of our documents. We're hoping for a design that resonates confidence, reliability and experience.
The design must include the firm name: Dorrance & Pike, PLLC. We would like the PLLC to be small compared to the Dorrance & Pike graphic. We also want to incorporate the attorney names: Ulric Dorrance, Janet Pike, and Lyle Hagberg. Our current letterhead has our contact info in the footer at the bottom of the page. We like that design, but are open to the idea of having it at the top. We'll leave that at the discretion of the designer. Our contact info is as follows: 472 S. Larchmont Avenue, Suite 315 Bellingham, WA 98117 Phone: 360-514-2967, Fax: 360-521-6079, and our website: www.dorrancepike-law.example
Target Market(s)
Clients, courts, other legal offices, doctors offices. These are the people who see our letterhead most frequently. It's not so much for marketing purposes, mainly so that we have a professional image when sending out documents.
Industry/Entity Type
Law Firm
Contact Information for Business Card
On the back of the business card: it can be designed, or be a template for filling in appointment reminder information (i.e. date, time, etc)
Colors
Designer to choose colors to be used in the design.
Requirements
Must have
- Must have our firm name at the top.
- Must include the attorney names.
- Must have all of our contact information (can be at top or bottom - whatever looks best with the design)
Nice to have
- A strong, confident design
Should not have
- We don't want the design to be playful, cartoony or busy.

```html
<!DOCTYPE html>
<html lang="en">
<head>
<meta charset="utf-8">
<title>Dorrance &amp; Pike, PLLC — Stationery</title>
<link rel="stylesheet" href="https://fonts.googleapis.com/css2?family=Roboto+Condensed:wght@400&family=Lato:wght@400;700&family=Roboto:wght@400;500&display=swap">
<style>
  :root {
    --backdrop: #e3e3e3;
    --paper: #f2f2f2;
    --ink: #3a3a3a;
    --ink-soft: #4a4a4a;
    --rule: #3a3a3a;
    --tab: #3b3b3b;
  }
  * { box-sizing: border-box; margin: 0; padding: 0; }
  html, body { width: 1146px; height: 1200px; overflow: hidden; }
  body { background: var(--backdrop); position: relative; color: var(--ink); }

  .letterhead {
    position: absolute; left: 30px; top: 136px;
    width: 660px; height: 928px;
    background: var(--paper);
    box-shadow: 0 12px 34px rgba(0,0,0,0.22);
  }
  .firm-name {
    font-family: "Roboto Condensed", sans-serif;
    font-weight: 400; color: var(--ink);
    white-space: nowrap; line-height: 1;
  }
  .letterhead .firm-name { position: absolute; left: 60px; top: 92px; font-size: 26px; }

  .attorneys {
    position: absolute; right: 55px; top: 78px;
    list-style: none; text-align: right;
    font-family: "Roboto Condensed", sans-serif; font-size: 15.5px; line-height: 18.5px;
    color: var(--ink);
  }
  .edge-tab { position: absolute; right: 0; top: 78px; width: 15px; height: 56px; background: var(--tab); }

  .letter-body {
    position: absolute; left: 60px; top: 276px; width: 550px;
    font-family: "Lato", sans-serif; font-size: 10px; line-height: 13px; color: var(--ink-soft);
  }
  .salutation { font-weight: 700; margin-bottom: 27px; color: var(--ink); }
  .letter-body p { text-align: justify; margin-bottom: 13px; }
  .signature { margin-top: 14px; line-height: 14px; }

  .letter-footer {
    position: absolute; left: 58px; right: 44px; top: 836px;
    border-top: 1px solid var(--rule); padding-top: 9px;
    display: flex; justify-content: space-between;
    font-family: "Roboto", sans-serif; font-size: 11px; line-height: 14.5px; color: var(--ink-soft);
  }
  .letter-footer .address { font-style: normal; }
  .letter-footer .contact { text-align: right; }
  .label { font-weight: 500; color: var(--ink); }

  .business-card {
    position: absolute; left: 720px; top: 700px;
    width: 400px; height: 229px;
    background: var(--paper);
    box-shadow: 0 10px 28px rgba(0,0,0,0.22);
  }
  .business-card .firm-name { position: absolute; left: 32px; top: 106px; font-size: 18px; }
  .card-divider { position: absolute; left: 215px; top: 58px; width: 1px; height: 120px; background: var(--rule); }
  .card-details {
    position: absolute; left: 228px; top: 56px;
    font-family: "Roboto", sans-serif; font-size: 10.5px; line-height: 13px; color: var(--ink-soft);
  }
  .card-details .person {
    font-family: "Roboto Condensed", sans-serif; font-size: 17px; line-height: 20px;
    color: var(--ink); margin-bottom: 6px;
  }
  .card-details .block { margin-bottom: 9px; }
  .card-details .web { font-weight: 500; color: var(--ink); margin-top: 12px; }
</style>
</head>
<body>

<section class="letterhead" aria-label="Letterhead">
  <div class="firm-name">Dorrance &amp; Pike, PLLC</div>
  <ul class="attorneys">
    <li>Ulric Dorrance</li>
    <li>Janet Pike</li>
    <li>Lyle Hagberg</li>
  </ul>
  <div class="edge-tab"></div>

  <div class="letter-body">
    <p class="salutation">Dear Mr. Smith,</p>
    <p>Lorem ipsum dolor sit amet, consectetur adipiscing elit. Donec orci purus, luctus vitae dignissim eu, iaculis sed purus. Vivamus faucibus, ipsum nec aliquet viverra, leo mauris condimentum ligula, sit amet sagittis enim ligula quis arcu. Nam egestas tortor id nisi porttitor mattis. In tortor ante, ultricies in suscipit a, tempus non massa. Vivamus et auctor mi.</p>
    <p>Fusce vel massa nulla. Phasellus nec eros mauris, et scelerisque orci. Donec malesuada orci vitae nulla accumsan porta a id massa. Quisque accumsan iaculis magna sit amet fringilla. Maecenas consequat, magna eget tincidunt semper, odio nibh rutrum mi, id feugiat ante nisi eu risus. Vestibulum nunc orci, rhoncus a placerat in, ultricies in mi. Cras mattis varius eros, vel fringilla nisi suscipit eget.</p>
    <p>Quisque scelerisque sagittis nulla at porttitor. Mauris a justo et tellus interdum tristique. Sed id augue vitae urna euismod commodo aliquet a quam. Pellentesque arcu velit, cursus et malesuada ut, consequat et diam. Nullam erat sem, rhoncus id ullamcorper vitae, rhoncus et arcu. In ultricies ultricies nulla, ut rutrum nisi iaculis at. Donec eu magna a metus ornare faucibus.</p>
    <p>Fusce aliquet faucibus ultricies. Morbi semper, est id tincidunt gravida, sem arcu adipiscing lacus, ac bibendum nulla leo eu purus. Quisque nec diam sed risus consectetur a ccumsan quis quis nibh. Vestibulum id purus lore</p>
    <p>Quisque accumsan iaculis magna sit amet fringilla. Maecenas consequat, magna eget tincidunt semper, odio nibh rutrum mi, id feugiat ante nisi eu risus. Vestibulum nunc orci, rhoncus a placerat in, ultricies in mi. Cras mattis varius eros, vel fringilla nisi suscipit eget.</p>
    <p>Quisque scelerisque sagittis nulla at porttitor. Mauris a justo et tellus interdum tristique. Sed id augue vitae urna euismod commodo aliquet a quam. Pellentesque arcu velit, cursus et malesuada ut</p>
    <p>Quisque accumsan iaculis magna sit amet fringilla. Maecenas consequat, magna eget tincidunt semper, odio nibh rutrum mi, id feugiat ante nisi eu risus.</p>
    <p class="signature">John Doe<br>Co-Founder &amp; CEO</p>
  </div>

  <footer class="letter-footer">
    <address class="address">
      472 S. Larchmont Avenue<br>Suite 315<br>Bellingham, WA 98117
    </address>
    <div class="contact">
      <span class="label">P:</span> 360-514-2967<br>
      <span class="label">F:</span> 360-521-6079<br>
      www.dorrancepike-law.example
    </div>
  </footer>
</section>

<section class="business-card" aria-label="Business card">
  <div class="firm-name">Dorrance &amp; Pike, PLLC</div>
  <div class="card-divider"></div>
  <div class="card-details">
    <div class="person">Ulric Dorrance</div>
    <div class="block">472 S. Larchmont Avenue<br>Suite 315,<br>Bellingham, WA 98117</div>
    <div class="block"><span class="label">P:</span> 360-514-2967<br><span class="label">F:</span> 360-521-6079</div>
    <div class="web">www.dorrancepike-law.example</div>
  </div>
</section>

</body>
</html>
```